Pain cream backed by Pro-Athletes "Glacier Ember"

Looking to revamp the label brand.
It's an all-natural pain gel. It heats then cools. Looking for a very sharp look that gets the point of the product use across.
Eveyrthing about the original label can be changed except for the text. It still needs to have the same information but can be any color, font whatever.,
I'll need pdf's and ai files of the design.
Label Size die line is attached.
Original Label is attached.

```html
<!DOCTYPE html>
<html lang="en">
<head>
<meta charset="utf-8">
<title>Glacier Ember – Label</title>
<link rel="stylesheet" href="https://fonts.googleapis.com/css2?family=Michroma&family=Montserrat:wght@400;500&display=swap">
<style>
  :root {
    --canvas: #dcdcdc;
    --label-black: #0c0c0d;
    --label-charcoal: #4a4a4b;
    --ice-deep: #1a2c7a;
    --ice-bright: #1fa3e6;
    --ember-light: #f2923f;
    --ember-mid: #c0603a;
    --ember-hot: #f0641a;
    --silver: #c9ccd1;
    --white: #ffffff;
    --pattern-dark: #1b1b1d;
  }
  * { margin: 0; padding: 0; box-sizing: border-box; }
  html, body {
    width: 1200px;
    height: 884px;
    overflow: hidden;
    background: var(--canvas);
  }
  .label {
    position: absolute;
    left: 370px;
    top: 122px;
    width: 460px;
    height: 640px;
    overflow: hidden;
    border-radius: 4px;
    box-shadow: 0 18px 40px rgba(0,0,0,0.18);
  }
  .label-art {
    position: absolute;
    inset: 0;
    width: 460px;
    height: 640px;
    display: block;
  }
  .brand-name {
    position: absolute;
    left: 0;
    right: 0;
    top: 150px;
    text-align: center;
    font-family: "Michroma", sans-serif;
    font-size: 38px;
    line-height: 1.25;
    letter-spacing: 6px;
    color: var(--silver);
  }
  .tagline {
    position: absolute;
    left: 0;
    right: 0;
    top: 480px;
    text-align: center;
    font-family: "Montserrat", sans-serif;
    font-weight: 500;
    font-size: 19px;
    line-height: 1.2;
    letter-spacing: 3px;
    color: var(--white);
  }
  .volume {
    position: absolute;
    left: 0;
    right: 0;
    top: 600px;
    text-align: center;
    font-family: "Montserrat", sans-serif;
    font-weight: 400;
    font-size: 11px;
    letter-spacing: 0.5px;
    color: var(--white);
  }
</style>
</head>
<body>
  <main class="label">
    <svg class="label-art" viewBox="0 0 460 640" aria-hidden="false">
      <defs>
        <linearGradient id="label-ground" x1="0" y1="0" x2="1" y2="1">
          <stop offset="0" stop-color="var(--label-black)"/>
          <stop offset="0.35" stop-color="var(--label-charcoal)"/>
          <stop offset="1" stop-color="var(--label-black)"/>
        </linearGradient>
        <linearGradient id="ice-band" x1="0" y1="0" x2="1" y2="0">
          <stop offset="0" stop-color="var(--ice-deep)"/>
          <stop offset="0.5" stop-color="var(--ice-bright)"/>
          <stop offset="1" stop-color="var(--ice-deep)"/>
        </linearGradient>
        <linearGradient id="ember-panel" x1="0" y1="0" x2="1" y2="1">
          <stop offset="0" stop-color="var(--ember-light)"/>
          <stop offset="0.5" stop-color="var(--ember-mid)"/>
          <stop offset="1" stop-color="var(--ember-hot)"/>
        </linearGradient>
      </defs>

      <rect class="label-ground" width="460" height="640" fill="url(#label-ground)"/>

      <path class="ice-band" d="M0,300 L130,350 L330,350 L460,300 L460,410 L330,445 L130,445 L0,410 Z"
            fill="url(#ice-band)" stroke="var(--silver)" stroke-width="3"/>

      <g role="img" aria-label="Fine curved line pattern, left side">
        <path d="M0,410 L70,428 L135,640 L0,640 Z" fill="var(--pattern-dark)"/>
      </g>
      <g role="img" aria-label="Fine curved line pattern, right side">
        <path d="M460,410 L390,428 L325,640 L460,640 Z" fill="var(--pattern-dark)"/>
      </g>

      <path class="ember-panel" d="M70,428 L130,445 L330,445 L390,428 L325,640 L135,640 Z"
            fill="url(#ember-panel)" stroke="var(--silver)" stroke-width="3"/>
    </svg>

    <h1 class="brand-name">GLACIER<br>EMBER</h1>
    <p class="tagline">GETS YOU<br>BACK UP</p>
    <p class="volume">100 ML (3.2oz)</p>
  </main>
</body>
</html>
```